Label design for unique cold brew coffee product

Require a label for front and back of a clear glass flint flask bottle. This will hold our speciality cold brew coffee. the label is to have your logo and represent our brand of being rustic, industrial, funky, mechanical etc as per our attached logo.

look forward to seeing the funky cool designs that will help bring our awesome product to market.

Target Market(s)

Hipsters, coffee connoisseurs, and one that enjoys a fine coffee.

Industry/Entity Type

Cafe

Requirements
Must have
• Brand recognition, staying true to the essence of what we are about, producing fine speciality cold brew coffee. Must have an rustic, industrial, funky, mechanical feel to be aligned with the logo.
• Please ensure the following is included and is editable on the label:
• Ingredients: Specialty Coffee & Filtered Water
• Brewed on :
• Keep Refrigerated
• Facebook, instagram etc logo
• Volume: 200ml etc
• Website: www.brewlantern.com.au
• Origin of the coffee
Should not have
• no bright colours

```html
<!DOCTYPE html>
<html lang="en">
<head>
<meta charset="utf-8">
<title>Brew Lantern Cold Brew Labels</title>
<link href="https://fonts.googleapis.com/css2?family=Passion+One:wght@400;700&family=Saira:wght@200;400&family=Roboto+Condensed:ital,wght@0,400;0,700;1,400&display=swap" rel="stylesheet">
<style>
  :root {
    --page: #ffffff;
    --rim: #3a2418;
    --panel-dark: #1b130e;
    --panel-mid: #5e4129;
    --cream: #f6eebb;
    --ink: #2a1a10;
    --bean: #8a4a22;
    --bean-light: #c27a3e;
    --dash: #c9b98a;
  }
  * { box-sizing: border-box; margin: 0; padding: 0; }
  html, body { width: 1200px; height: 800px; overflow: hidden; background: var(--page); }
  .canvas { position: relative; width: 1200px; height: 800px; }
  .label { position: absolute; top: 20px; width: 525px; height: 760px; }
  .label--front { left: 56px; }
  .label--back { left: 620px; }
  .label__shape { position: absolute; inset: 0; width: 525px; height: 760px; }
  .abs { position: absolute; }
  .brand-name {
    left: 0; width: 525px; text-align: center;
    font-family: "Passion One", sans-serif; font-weight: 400;
    color: var(--cream); letter-spacing: 3px; line-height: 1;
  }
  .label--front .brand-name { top: 180px; font-size: 54px; }
  .label--back .brand-name { top: 118px; font-size: 40px; }
  .beans {
    border-radius: 40%;
    background: radial-gradient(ellipse at center, var(--bean-light) 0%, var(--bean) 45%, rgba(138,74,34,0) 75%);
  }
  .rule { height: 1px; background: var(--dash); opacity: .8; }
  .pill {
    background: var(--cream); color: var(--ink); border-radius: 8px;
    font-family: "Roboto Condensed", sans-serif; text-align: center;
  }
  .title-cold {
    left: 0; width: 525px; text-align: center;
    font-family: "Passion One", sans-serif; font-weight: 700;
    color: var(--cream); line-height: 1;
    text-shadow: 3px 3px 0 #000;
  }
  .title-coffee {
    left: 0; width: 525px; text-align: center;
    font-family: "Saira", sans-serif; font-weight: 200;
    color: var(--cream); line-height: 1;
  }
  .volume { font-family: "Saira", sans-serif; font-weight: 400; color: var(--cream); font-size: 18px; line-height: 1; }
  .info-table {
    left: 94px; top: 324px; width: 336px; height: 168px;
    border: 1.5px dashed var(--dash); background: rgba(90,70,52,.45);
    font-family: "Roboto Condensed", sans-serif;
  }
  .info-table__head {
    height: 33px; border-bottom: 1.5px dashed var(--dash);
    text-align: center; font-weight: 700; font-size: 16px; color: var(--ink);
    line-height: 33px; background: rgba(201,185,138,.35);
  }
  .info-table__ingredients {
    height: 48px; border-bottom: 1.5px dashed var(--dash);
    text-align: center; color: var(--cream); font-size: 19px; line-height: 48px;
    font-family: "Saira", sans-serif;
  }
  .info-table__row { display: flex; height: 84px; }
  .info-table__cell { flex: 1; }
  .info-table__cell + .info-table__cell { border-left: 1.5px dashed var(--dash); }
  .info-table__cell-head {
    height: 33px; border-bottom: 1.5px dashed var(--dash);
    text-align: center; line-height: 33px; font-weight: 700; font-size: 15px; color: var(--ink);
    background: rgba(201,185,138,.3);
  }
  .social {
    left: 53px; top: 526px; width: 420px; height: 30px;
    display: flex; align-items: center; justify-content: center; gap: 8px;
    font-family: "Roboto Condensed", sans-serif; font-size: 13px;
  }
  .social__mark { width: 16px; height: 16px; background: var(--ink); border-radius: 2px; }
  .social__name { font-weight: 700; font-size: 16px; font-style: normal; }
  .flourish {
    left: 200px; top: 690px; width: 124px; height: 44px; border-radius: 50%;
    background: linear-gradient(90deg, #5a3a22, #8a5a30, #5a3a22);
  }
</style>
</head>
<body>
<div class="canvas">

  <section class="label label--front">
    <svg class="label__shape" viewBox="0 0 525 760" aria-hidden="true">
      <defs>
        <radialGradient id="panelFront" cx="50%" cy="35%" r="70%">
          <stop offset="0" stop-color="#6b4a30"/>
          <stop offset=".55" stop-color="#3a271a"/>
          <stop offset="1" stop-color="#1b130e"/>
        </radialGradient>
      </defs>
      <path d="M12 80 Q5 82 6 95 L18 690 Q20 705 35 705 L170 700 Q200 758 262 758 Q325 758 355 700 L490 705 Q505 705 507 690 L519 95 Q520 82 512 80 L360 70 Q320 2 262 2 Q205 2 165 70 Z" fill="#fff" stroke="#3a2418" stroke-width="4"/>
      <path d="M24 95 L185 85 Q220 22 262 22 Q305 22 340 85 L500 95 L490 690 L30 690 Z" fill="url(#panelFront)"/>
      <ellipse cx="262" cy="714" rx="98" ry="40" fill="#fff"/>
    </svg>
    <div class="abs brand-name">BREW LANTERN</div>
    <div class="abs beans" style="left:70px;top:410px;width:385px;height:60px" role="img" aria-label="Row of roasted coffee beans"></div>
    <div class="abs rule" style="left:90px;top:473px;width:345px"></div>
    <div class="abs pill" style="left:150px;top:466px;width:210px;height:14px"></div>
    <div class="abs title-cold" style="top:492px;font-size:72px">COLD BREW</div>
    <div class="abs title-coffee" style="top:570px;font-size:76px">COFFEE</div>
    <div class="abs rule" style="left:90px;top:657px;width:345px"></div>
    <div class="abs pill" style="left:160px;top:649px;width:205px;height:17px;font-size:12px;font-weight:700;line-height:17px">www.brewlantern.com.au</div>
    <div class="abs volume" style="left:432px;top:664px">200 ml</div>
    <div class="abs flourish" role="img" aria-label="Decorative brown flourish"></div>
  </section>

  <section class="label label--back">
    <svg class="label__shape" viewBox="0 0 525 760" aria-hidden="true">
      <defs>
        <radialGradient id="panelBack" cx="50%" cy="30%" r="70%">
          <stop offset="0" stop-color="#6b4a30"/>
          <stop offset=".55" stop-color="#3a271a"/>
          <stop offset="1" stop-color="#1b130e"/>
        </radialGradient>
      </defs>
      <path d="M12 80 Q5 82 6 95 L18 690 Q20 705 35 705 L170 700 Q200 758 262 758 Q325 758 355 700 L490 705 Q505 705 507 690 L519 95 Q520 82 512 80 L360 70 Q320 2 262 2 Q205 2 165 70 Z" fill="#fff" stroke="#3a2418" stroke-width="4"/>
      <path d="M24 95 L185 85 Q220 22 262 22 Q305 22 340 85 L500 95 L490 690 L30 690 Z" fill="url(#panelBack)"/>
      <ellipse cx="262" cy="714" rx="98" ry="40" fill="#fff"/>
    </svg>
    <div class="abs brand-name">BREW LANTERN</div>
    <div class="abs beans" style="left:100px;top:246px;width:325px;height:30px" role="img" aria-label="Row of roasted coffee beans"></div>
    <div class="abs rule" style="left:80px;top:281px;width:365px"></div>
    <div class="abs pill" style="left:158px;top:270px;width:210px;height:22px;font-size:15px;font-weight:700;line-height:22px">www.brewlantern.com.au</div>
    <div class="abs info-table">
      <div class="info-table__head">INGREDIENTS:</div>
      <div class="info-table__ingredients">Specialty Coffee &amp; Filtered Water</div>
      <div class="info-table__row">
        <div class="info-table__cell"><div class="info-table__cell-head">BREWED ON:</div></div>
        <div class="info-table__cell"><div class="info-table__cell-head">ORIGIN:</div></div>
      </div>
    </div>
    <div class="abs pill" style="left:53px;top:502px;width:420px;height:17px;font-size:12px;line-height:17px">KEEP REFRIGERATED</div>
    <div class="abs pill social">
      <span class="social__mark"></span>
      <i>Find us on social media:</i>
      <span class="social__name">BREW LANTERN</span>
    </div>
    <div class="abs rule" style="left:50px;top:570px;width:425px"></div>
    <div class="abs title-cold" style="top:582px;font-size:44px">COLD BREW</div>
    <div class="abs title-coffee" style="top:622px;font-size:46px">COFFEE</div>
    <div class="abs volume" style="left:420px;top:660px">200 ml</div>
    <div class="abs flourish" role="img" aria-label="Decorative brown flourish"></div>
  </section>

</div>
</body>
</html>
```